Luxury Business Card Design

We need a business card design for a law firm that look sophisticated and luxury

Target Market(s)

Australian legal markets

Industry/Entity Type

Legal

Contact Information for Business Card

Attached

Requirements
Must have
• Logo, head office address on front side and 2 other addresses on the back side.
Nice to have
• Please see below our current business card. Need something more sophisticated and luxury feel

```html
<!DOCTYPE html>
<html lang="en">
<head>
<meta charset="utf-8">
<title>Ashbury Legal – Business Card</title>
<link rel="stylesheet" href="https://fonts.googleapis.com/css2?family=Cinzel:wght@500&family=Crimson+Text:wght@400;600&family=Roboto:wght@400;500;700&display=swap">
<style>
  :root {
    --backdrop: #ababab;
    --cream: #efebdf;
    --forest: #03281a;
    --forest-ink: #0a2a1a;
    --gold: #cfa75a;
    --muted: #9a968c;
    --white: #ffffff;
  }
  * { margin: 0; padding: 0; box-sizing: border-box; }
  html, body { width: 1200px; height: 1000px; overflow: hidden; }
  body { background: var(--backdrop); position: relative; font-family: 'Roboto', sans-serif; }

  .card {
    position: absolute; left: 294px; width: 613px; height: 352px;
    overflow: hidden;
    box-shadow: 0 22px 45px rgba(0,0,0,.38);
  }
  .card--front { top: 109px; background: var(--cream); }
  .card--back { top: 532px; background: var(--forest); color: var(--white); }

  /* Front */
  .brand-ring {
    position: absolute; left: 244px; top: 64px; width: 114px; height: 114px;
    border: 5px solid var(--gold); border-radius: 50%;
  }
  .brand-name {
    position: absolute; left: 0; right: 0; top: 192px; text-align: center;
    font-family: 'Cinzel', serif; font-weight: 500; color: var(--forest-ink);
    font-size: 50px; line-height: 56px; letter-spacing: 1px;
  }
  .brand-name .sub { display: block; font-size: 22px; line-height: 30px; letter-spacing: 12px; padding-left: 12px; }
  .website {
    position: absolute; left: 0; right: 0; top: 294px; text-align: center;
    font-size: 19px; color: var(--muted);
  }
  .gold-band { position: absolute; left: 0; right: 0; bottom: 0; height: 11px; background: var(--gold); }

  /* Back */
  .faint-ring {
    position: absolute; left: 322px; top: -40px; width: 330px; height: 330px;
    border: 1.5px solid rgba(255,255,255,.1); border-radius: 50%;
  }
  .person { position: absolute; left: 40px; top: 50px; width: 198px; text-align: center; }
  .person__name { font-family: 'Crimson Text', serif; font-size: 31px; line-height: 36px; letter-spacing: .5px; }
  .person__name .surname { color: var(--gold); }
  .person__title { font-family: 'Crimson Text', serif; font-weight: 600; font-size: 14px; line-height: 16px; }
  .divider { display: flex; align-items: center; justify-content: center; gap: 6px; margin: 15px 0 14px; }
  .divider .rule { width: 30px; height: 1px; background: var(--gold); margin: 0 4px; }
  .divider svg { display: block; }
  .contact { font-size: 12.5px; line-height: 15px; }

  .offices { position: absolute; left: 30px; top: 240px; display: flex; }
  .office { width: 182px; text-align: center; font-size: 11.8px; line-height: 14.5px; }
  .office:nth-child(2) { width: 180px; }
  .office__pin { display: block; margin: 0 auto 7px; }
  .office__heading { color: var(--gold); font-weight: 700; font-size: 13.5px; line-height: 16px; letter-spacing: .3px; }
  .office__phone { font-weight: 700; }
  .office__phone svg { vertical-align: -1px; margin-right: 1px; }
</style>
</head>
<body>

<section class="card card--front">
  <div class="brand-ring"></div>
  <div class="brand-name">ASHBURY<span class="sub">LEGAL</span></div>
  <div class="website">ashburylegal.com.au</div>
  <div class="gold-band"></div>
</section>

<section class="card card--back">
  <div class="faint-ring"></div>

  <div class="person">
    <div class="person__name">DANIEL <span class="surname">MERCER</span></div>
    <div class="person__title">Director &amp; Principal Solicitor</div>
    <div class="person__title">MBA, Juris Doctor</div>
    <div class="divider">
      <span class="rule"></span>
      <svg width="14" height="10" viewBox="0 0 14 10"><rect width="14" height="10" fill="var(--gold)"/><path d="M0 0 L7 6 L14 0" stroke="var(--forest)" stroke-width="1.3" fill="none"/></svg>
      <svg width="8" height="13" viewBox="0 0 8 13"><rect x=".75" y=".75" width="6.5" height="11.5" rx="1.2" stroke="var(--gold)" stroke-width="1.5" fill="none"/><circle cx="4" cy="10.3" r=".8" fill="var(--gold)"/></svg>
      <svg width="12" height="12" viewBox="0 0 24 24"><path fill="var(--gold)" d="M6.6 10.8a15.1 15.1 0 0 0 6.6 6.6l2.2-2.2c.3-.3.7-.4 1-.2 1.1.4 2.3.6 3.6.6.6 0 1 .4 1 1V20c0 .6-.4 1-1 1A17 17 0 0 1 3 4c0-.6.4-1 1-1h3.5c.6 0 1 .4 1 1 0 1.3.2 2.5.6 3.6.1.3 0 .7-.2 1z"/></svg>
      <span class="rule"></span>
    </div>
    <div class="contact">daniel@ashburylegal.com.au</div>
    <div class="contact">+61 0400 000 123</div>
    <div class="contact">+61 7 3000 0148</div>
  </div>

  <div class="offices">
    <div class="office">
      <svg class="office__pin" width="11" height="14" viewBox="0 0 12 16"><path fill="var(--gold)" d="M6 0a6 6 0 0 0-6 6c0 4.5 6 10 6 10s6-5.5 6-10a6 6 0 0 0-6-6zm0 8.3A2.3 2.3 0 1 1 6 3.7a2.3 2.3 0 0 1 0 4.6z"/></svg>
      <div class="office__heading">BRISBANE OFFICE</div>
      <div>Level 2/88 Harlow Terrace</div>
      <div>Kelvin Hill QLD 4002</div>
      <div class="office__phone"><svg width="10" height="10" viewBox="0 0 24 24"><path fill="var(--gold)" d="M6.6 10.8a15.1 15.1 0 0 0 6.6 6.6l2.2-2.2c.3-.3.7-.4 1-.2 1.1.4 2.3.6 3.6.6.6 0 1 .4 1 1V20c0 .6-.4 1-1 1A17 17 0 0 1 3 4c0-.6.4-1 1-1h3.5c.6 0 1 .4 1 1 0 1.3.2 2.5.6 3.6.1.3 0 .7-.2 1z"/></svg>+61 7 3000 0148</div>
    </div>
    <div class="office">
      <svg class="office__pin" width="11" height="14" viewBox="0 0 12 16"><path fill="var(--gold)" d="M6 0a6 6 0 0 0-6 6c0 4.5 6 10 6 10s6-5.5 6-10a6 6 0 0 0-6-6zm0 8.3A2.3 2.3 0 1 1 6 3.7a2.3 2.3 0 0 1 0 4.6z"/></svg>
      <div class="office__heading">MELBOURNE OFFICE</div>
      <div>Suite 310, Carrow Chambers</div>
      <div>212 Bexley Lane</div>
      <div>MELBOURNE VIC 3000</div>
      <div class="office__phone"><svg width="10" height="10" viewBox="0 0 24 24"><path fill="var(--gold)" d="M6.6 10.8a15.1 15.1 0 0 0 6.6 6.6l2.2-2.2c.3-.3.7-.4 1-.2 1.1.4 2.3.6 3.6.6.6 0 1 .4 1 1V20c0 .6-.4 1-1 1A17 17 0 0 1 3 4c0-.6.4-1 1-1h3.5c.6 0 1 .4 1 1 0 1.3.2 2.5.6 3.6.1.3 0 .7-.2 1z"/></svg>+61 3 9000 0262</div>
    </div>
    <div class="office">
      <svg class="office__pin" width="11" height="14" viewBox="0 0 12 16"><path fill="var(--gold)" d="M6 0a6 6 0 0 0-6 6c0 4.5 6 10 6 10s6-5.5 6-10a6 6 0 0 0-6-6zm0 8.3A2.3 2.3 0 1 1 6 3.7a2.3 2.3 0 0 1 0 4.6z"/></svg>
      <div class="office__heading">PERTH OFFICE</div>
      <div>Suite 12, 47 Marlow Highway</div>
      <div>WESTBROOK WA 6011</div>
      <div class="office__phone"><svg width="10" height="10" viewBox="0 0 24 24"><path fill="var(--gold)" d="M6.6 10.8a15.1 15.1 0 0 0 6.6 6.6l2.2-2.2c.3-.3.7-.4 1-.2 1.1.4 2.3.6 3.6.6.6 0 1 .4 1 1V20c0 .6-.4 1-1 1A17 17 0 0 1 3 4c0-.6.4-1 1-1h3.5c.6 0 1 .4 1 1 0 1.3.2 2.5.6 3.6.1.3 0 .7-.2 1z"/></svg>+61 400 000 123</div>
    </div>
  </div>
</section>

</body>
</html>
```